Redesign website

I purchased a business a few months ago and I'm in the process on rebranding everything and creating a new website. I want the new website completely different with 5 pages and nice pictures on every page. Also I want my new logo and colors to included on the site.
Current Site https://www.bristlewoodpetsinc.com

Industry/Entity Type

Dog Sitting

Coding

Coded - Design and coding required

Number of Pages Required

5+ page

Requirements
Must have
• I have pictures and a video I can shared to use for the website.
Just as the current site it should have an option to be taken to the site I have to make reservations.
Nice to have
• Would be nice to have social media intergrations

```html
<!DOCTYPE html>
<html lang="en">
<head>
<meta charset="utf-8">
<title>Bristlewood Pets – Our Services</title>
<link rel="stylesheet" href="https://fonts.googleapis.com/css2?family=Lobster&family=Open+Sans:wght@300;400;600;700&display=swap">
<style>
:root{
  --sky:#1ab3e8;
  --teal:#00b6c9;
  --magenta:#c0137f;
  --ink:#222;
  --body:#555;
  --muted:#8a8a8a;
  --line:#e4e4e4;
  --mist:#f2f2f2;
  --white:#fff;
  --script:'Lobster',cursive;
  --sans:'Open Sans',Arial,sans-serif;
}
*{box-sizing:border-box;margin:0;padding:0}
html,body{width:1200px;height:3039px;overflow:hidden;background:var(--white);font-family:var(--sans);color:var(--body)}
.page{position:relative;width:1200px;height:3039px}
.abs{position:absolute}

/* top bar */
.topbar{position:absolute;left:0;top:0;width:1200px;height:56px;background:var(--sky);color:var(--white);font-size:13px}
.topbar .edge{position:absolute;left:0;bottom:0;width:1200px;height:8px}
.topbar .info{position:absolute;left:161px;top:23px;display:flex;gap:22px;align-items:center}
.topbar .info span{display:flex;align-items:center;gap:8px}
.social{display:flex;gap:12px;align-items:center}
.topbar .social{position:absolute;right:162px;top:26px}
.social i{display:block;width:11px;height:11px;border-radius:2px;background:currentColor;opacity:.95}
.social i.round{border-radius:50%}

/* header */
.brand{display:flex;align-items:center;gap:6px;font-family:var(--script);color:var(--magenta);font-size:22px}
.brand b{display:block;width:26px;height:26px;border-radius:50%;background:var(--teal)}
.header .brand{position:absolute;left:161px;top:86px}
.nav{position:absolute;top:96px;left:0;font-size:14px;color:#333}
.nav a{position:absolute;color:#333;text-decoration:none;white-space:nowrap}
.nav .search{position:absolute;left:1025px;top:-1px}

/* banner */
.banner{position:absolute;left:0;top:146px;width:1200px;height:156px;background:linear-gradient(90deg,#22231a 0%,#2c2c20 55%,#3b3628 78%,#2a2a20 100%)}
.banner h1{position:absolute;left:161px;top:52px;font-family:var(--script);font-weight:400;font-size:31px;color:var(--white)}
.crumb{position:absolute;left:901px;top:60px;width:137px;height:36px;border:2px solid var(--white);border-radius:20px;color:var(--white);font-size:11px;font-weight:600;display:flex;align-items:center;justify-content:center;gap:6px}

/* intro */
.intro{position:absolute;left:0;top:364px;width:1200px;text-align:center;font-weight:300;font-size:28px;line-height:33px;color:#444}

/* feature cards */
.card{position:absolute;width:427px;height:149px;border:1px solid var(--line);background:var(--white)}
.card .icon{position:absolute;left:24px;top:34px;width:48px;height:48px}
.card h3{position:absolute;left:104px;top:33px;font-family:var(--script);font-weight:400;font-size:15px;color:var(--ink)}
.card p{position:absolute;left:104px;top:62px;width:300px;font-size:11px;line-height:18px;color:var(--body)}

/* offers */
.offers{position:absolute;left:0;top:1056px;width:1200px;height:984px;background:var(--mist)}
.divider{position:absolute;left:0;width:1200px;display:flex;justify-content:center;align-items:center;gap:8px}
.divider .dots{width:26px;height:6px;background:radial-gradient(circle,currentColor 1px,transparent 1.4px) 0 0/3px 3px}
.divider .dot{width:12px;height:12px;border-radius:50%;background:currentColor}
.tagline{position:absolute;left:0;width:1200px;text-align:center;font-family:var(--script);font-size:10px}
.heading{position:absolute;left:0;width:1200px;text-align:center;font-family:var(--script);font-weight:400;font-size:27px}
.offer{position:absolute;width:277px;text-align:center}
.offer .photo{width:277px;height:231px}
.offer h3{margin-top:16px;font-family:var(--script);font-weight:400;font-size:17px;color:var(--ink)}
.offer p{margin:10px auto 0;width:240px;font-size:11px;line-height:16.5px;color:var(--body)}
.offer a{display:block;margin-top:13px;font-size:10.5px;font-weight:700;color:var(--sky);text-decoration:none;letter-spacing:.3px}

/* appointment */
.appointment{position:absolute;left:0;top:2040px;width:1200px;height:609px;background:var(--teal);color:var(--white)}
.field{position:absolute;width:272px;height:37px;border-radius:20px;background:var(--white);color:#888;font-size:11px;padding:11px 0 0 19px}
.field.message{width:877px;height:104px;border-radius:22px;padding-top:14px}
.send{position:absolute;left:517px;top:423px;width:164px;height:41px;border-radius:21px;background:var(--magenta);color:var(--white);font-family:var(--script);font-size:13px;display:flex;align-items:center;justify-content:center}

/* footer */
.footer{position:absolute;left:0;top:2649px;width:1200px;height:390px}
.footer h4{position:absolute;font-family:var(--script);font-weight:400;font-size:13px;color:var(--ink)}
.footer .about{position:absolute;left:161px;top:160px;width:272px;font-size:11px;line-height:18px}
.links{position:absolute;left:465px;top:159px;list-style:none;font-size:11px;color:#444}
.links li{height:22.5px;display:flex;align-items:center;gap:9px}
.links li::before{content:"";width:8px;height:8px;border-radius:50%;background:#cfcfcf}
.post{position:absolute;left:615px;display:flex;gap:8px}
.post .thumb{width:60px;height:60px;flex:none}
.post strong{display:block;font-size:11px;line-height:16px;color:#333;width:110px}
.post small{display:block;font-size:9px;color:var(--muted);margin-top:3px}
.touch{position:absolute;left:842px;font-size:11px;line-height:18px;display:flex;gap:14px}
.touch svg{flex:none}
.rule{position:absolute;left:161px;top:323px;width:877px;height:1px;background:var(--line)}
.copy{position:absolute;left:0;top:350px;width:1200px;text-align:center;font-size:11px;color:var(--muted)}
</style>
</head>
<body>
<div class="page">

  <!-- top bar -->
  <div class="topbar">
    <div class="info">
      <span><svg width="9" height="12" viewBox="0 0 9 12"><path d="M4.5 0A4.5 4.5 0 0 0 0 4.5C0 8 4.5 12 4.5 12S9 8 9 4.5A4.5 4.5 0 0 0 4.5 0zm0 6.3a1.8 1.8 0 1 1 0-3.6 1.8 1.8 0 0 1 0 3.6z" fill="#fff"/></svg>Lorem ipsum dolor sit amet</span>
      <span><svg width="12" height="12" viewBox="0 0 12 12"><path d="M2.4 0.5l2 2-1 1.6c.7 1.5 1.9 2.7 3.5 3.5l1.6-1 2 2-1.2 2.2C5.3 10.6 1.4 6.7.2 1.7z" fill="#fff"/></svg>+(1) 234 567 8900</span>
      <span><svg width="13" height="10" viewBox="0 0 13 10"><rect width="13" height="10" rx="1" fill="#fff"/><path d="M0.5 1l6 4.5 6-4.5" stroke="#1ab3e8" fill="none"/></svg>info@example.com</span>
    </div>
    <div class="social"><i></i><i class="round"></i><i></i><i></i><i class="round"></i></div>
    <svg class="edge" viewBox="0 0 1200 8" preserveAspectRatio="none"><path d="M0 8V4l20 3 18-4 25 4 30-3 22 3 28-4 24 4 30-2 26 3 22-4 30 4 28-3 24 3 30-4 26 4 22-3 30 3 28-4 24 4 30-3 26 3 24-4 28 4 26-3 30 3 22-4 28 4 30-3 24 3 26-4 30 4 22-3 28 3 26-4 30 4 24-3 28 3 26-4 30 4 22-3 30 3 26-4 28 4 24-3 30 3 28-4 22 4 30-3 26 3 24-4 30 4 28-3 22 3 30-4 26 4 24-3 30 3 V8z" fill="#fff"/></svg>
  </div>

  <!-- header -->
  <header class="header">
    <div class="brand"><b></b>Bristlewood Pets</div>
    <nav class="nav">
      <a style="left:526px">Home</a>
      <a style="left:594px">About</a>
      <a style="left:662px">Services</a>
      <a style="left:741px">Photos</a>
      <a style="left:815px">Policies</a>
      <a style="left:891px">News</a>
      <a style="left:956px">Contact</a>
      <svg class="search" width="14" height="14" viewBox="0 0 14 14"><circle cx="5.8" cy="5.8" r="4.5" stroke="#222" stroke-width="2" fill="none"/><path d="M9 9l4 4" stroke="#222" stroke-width="2.2" stroke-linecap="round"/></svg>
    </nav>
  </header>

  <!-- banner -->
  <section class="banner" role="img" aria-label="Dark photo of a small terrier dog">
    <h1>Our Services</h1>
    <div class="crumb">Home <span>/</span> Services</div>
  </section>

  <h2 class="intro">We are Professionals to care for your pets &amp; giving<br>youpeace of mind about your pets</h2>

  <!-- feature cards -->
  <svg width="0" height="0" style="position:absolute">
    <defs>
      <g id="ico-groom"><circle cx="10" cy="36" r="6" stroke="#222" stroke-width="3" fill="none"/><circle cx="22" cy="40" r="6" stroke="#222" stroke-width="3" fill="none"/><path d="M12 31L24 6M20 35L6 10" stroke="#222" stroke-width="3" stroke-linecap="round"/><rect x="34" y="8" width="8" height="36" fill="#222"/><path d="M34 14h-4M34 20h-4M34 26h-4M34 32h-4M34 38h-4" stroke="#222" stroke-width="2"/></g>
      <g id="ico-paw"><ellipse cx="24" cy="31" rx="10" ry="8" stroke="#222" stroke-width="2.5" fill="none"/><circle cx="11" cy="20" r="4" stroke="#222" stroke-width="2.5" fill="none"/><circle cx="19" cy="11" r="4" stroke="#222" stroke-width="2.5" fill="none"/><circle cx="29" cy="11" r="4" stroke="#222" stroke-width="2.5" fill="none"/><circle cx="37" cy="20" r="4" stroke="#222" stroke-width="2.5" fill="none"/></g>
      <g id="ico-bowl"><path d="M4 32h40l-4 8H8z" stroke="#222" stroke-width="2.5" fill="none"/><path d="M8 32c0-10 7-16 16-16s16 6 16 16" stroke="#222" stroke-width="2.5" fill="none"/><rect x="17" y="22" width="14" height="6" rx="3" stroke="#222" stroke-width="2" fill="none"/></g>
    </defs>
  </svg>

  <div class="card" style="left:161px;top:475px"><svg class="icon" viewBox="0 0 48 48"><use href="#ico-groom"/></svg><h3>Pet Grooming</h3><p>Abore et dolore magna aliqua ut enim minim veniam quis nostrud exercitation ullamco laboris nisi aliquip eiusmod tempor incididunt labore.</p></div>
  <div class="card" style="left:611px;top:475px"><svg class="icon" viewBox="0 0 48 48"><use href="#ico-paw"/></svg><h3>Pet Adoption</h3><p>Abore et dolore magna aliqua ut enim minim veniam quis nostrud exercitation ullamco laboris nisi aliquip eiusmod tempor incididunt labore.</p></div>
  <div class="card" style="left:161px;top:648px"><svg class="icon" viewBox="0 0 48 48"><use href="#ico-paw"/></svg><h3>Pet Training</h3><p>Abore et dolore magna aliqua ut enim minim veniam quis nostrud exercitation ullamco laboris nisi aliquip eiusmod tempor incididunt labore.</p></div>
  <div class="card" style="left:611px;top:648px"><svg class="icon" viewBox="0 0 48 48"><use href="#ico-bowl"/></svg><h3>Pet Vaccination</h3><p>Abore et dolore magna aliqua ut enim minim veniam quis nostrud exercitation ullamco laboris nisi aliquip eiusmod tempor incididunt labore.</p></div>
  <div class="card" style="left:161px;top:822px"><svg class="icon" viewBox="0 0 48 48"><use href="#ico-groom"/></svg><h3>Pet Grooming</h3><p>Abore et dolore magna aliqua ut enim minim veniam quis nostrud exercitation ullamco laboris nisi aliquip eiusmod tempor incididunt labore.</p></div>
  <div class="card" style="left:611px;top:822px"><svg class="icon" viewBox="0 0 48 48"><use href="#ico-paw"/></svg><h3>Pet Adoption</h3><p>Abore et dolore magna aliqua ut enim minim veniam quis nostrud exercitation ullamco laboris nisi aliquip eiusmod tempor incididunt labore.</p></div>

  <!-- more service offers -->
  <section class="offers">
    <div class="divider" style="top:45px;color:#1ab3e8"><span class="dots"></span><span class="dot"></span><span class="dots"></span></div>
    <div class="tagline" style="top:75px;color:#444">Because We Really Care About Your Pets</div>
    <h2 class="heading" style="top:92px;color:var(--magenta)">More Service Offers</h2>

    <div class="offer" style="left:161px;top:156px"><div class="photo" role="img" aria-label="Terrier being groomed with scissors" style="background:linear-gradient(135deg,#d9c7ad,#b27a44 55%,#e8d8c6)"></div><h3>Pet Grooming</h3><p>Due thanks blissfully reverent that outside pled along some goldfish did chromatic gosh sloth sedas instead coincident</p><a>READ MORE</a></div>
    <div class="offer" style="left:461px;top:156px"><div class="photo" role="img" aria-label="Girl hugging a white fluffy dog" style="background:linear-gradient(135deg,#e8e2d6,#d9c8c0 45%,#c94a55 100%)"></div><h3>Pet Adoption</h3><p>Due thanks blissfully reverent that outside pled along some goldfish did chromatic gosh sloth sedas instead coincident</p><a>READ MORE</a></div>
    <div class="offer" style="left:761px;top:156px"><div class="photo" role="img" aria-label="Golden puppy on a red leash beside its owner" style="background:linear-gradient(135deg,#3f6f9e,#8aa6bf 50%,#d8c19a)"></div><h3>Pet Training</h3><p>Due thanks blissfully reverent that outside pled along some goldfish did chromatic gosh sloth sedas instead coincident</p><a>READ MORE</a></div>

    <div class="offer" style="left:161px;top:556px"><div class="photo" role="img" aria-label="Two small dogs being walked on leashes" style="background:linear-gradient(135deg,#9aa29a,#d9d4c8 50%,#4d6b3c)"></div><h3>Pet Sitting &amp; Walking</h3><p>Due thanks blissfully reverent that outside pled along some goldfish did chromatic gosh sloth sedas instead coincident</p><a>READ MORE</a></div>
    <div class="offer" style="left:461px;top:556px"><div class="photo" role="img" aria-label="Couple holding a small terrier" style="background:linear-gradient(135deg,#cbb59a,#8a6a4c 55%,#3e3a36)"></div><h3>Pet DayCare</h3><p>Due thanks blissfully reverent that outside pled along some goldfish did chromatic gosh sloth sedas instead coincident</p><a>READ MORE</a></div>
    <div class="offer" style="left:761px;top:556px"><div class="photo" role="img" aria-label="Vet and owner with a golden puppy" style="background:linear-gradient(135deg,#b7a37a,#e6ddd0 50%,#3b2a26)"></div><h3>Pet Vaccination</h3><p>Due thanks blissfully reverent that outside pled along some goldfish did chromatic gosh sloth sedas instead coincident</p><a>READ MORE</a></div>
  </section>

  <!-- appointment -->
  <section class="appointment">
    <div class="divider" style="top:45px;color:#fff"><span class="dots"></span><span class="dot"></span><span class="dots"></span></div>
    <div class="tagline" style="top:75px">Because We Really Care About Your Pets</div>
    <h2 class="heading" style="top:92px">Get An Appointment</h2>
    <div class="field" style="left:161px;top:162px">Name</div>
    <div class="field" style="left:464px;top:162px">Email</div>
    <div class="field" style="left:767px;top:162px">Phone</div>
    <div class="field" style="left:161px;top:221px">Date &nbsp;&amp; Time</div>
    <div class="field" style="left:464px;top:221px">Pet Category</div>
    <div class="field" style="left:767px;top:221px">Service Type</div>
    <div class="field message" style="left:161px;top:280px">Your Message...</div>
    <div class="send">Send Request</div>
  </section>

  <!-- footer -->
  <footer class="footer">
    <div class="brand" style="position:absolute;left:161px;top:76px"><b></b>Bristlewood Pets</div>
    <p class="about">Lorem ipsum dolor sit amet, consectetur adipiscing elit. Morbi placerat tellus at iaculis maximus. Maecenas tincidunt lacus quis suscipit fringilla. Ut sed turpis a lectus commodo vestibulum.</p>
    <div class="social" style="position:absolute;left:161px;top:254px;color:#8a8a8a"><i></i><i class="round"></i><i></i><i></i><i class="round"></i></div>

    <h4 style="left:465px;top:124px">Quick Links</h4>
    <ul class="links">
      <li>Home</li><li>About Us</li><li>Our Services</li><li>Our News</li><li>Our Policies</li><li>Contact Us</li>
    </ul>

    <h4 style="left:615px;top:124px">Recent Posts</h4>
    <div class="post" style="top:162px"><div class="thumb" role="img" aria-label="Dog with owner outdoors" style="background:linear-gradient(135deg,#7fb6d8,#c9a88a 60%,#b23a4a)"></div><div><strong>We Have Best Pet Grooming Services</strong><small>Apr 15, 2020</small></div></div>
    <div class="post" style="top:240px"><div class="thumb" role="img" aria-label="Dog with owner outdoors" style="background:linear-gradient(135deg,#7fb6d8,#c9a88a 60%,#b23a4a)"></div><div><strong>We Have Best Pet Grooming Services</strong><small>Apr 15, 2020</small></div></div>

    <h4 style="left:842px;top:124px">Get in Touch</h4>
    <div class="touch" style="top:158px"><svg width="14" height="19" viewBox="0 0 9 12"><path d="M4.5 0A4.5 4.5 0 0 0 0 4.5C0 8 4.5 12 4.5 12S9 8 9 4.5A4.5 4.5 0 0 0 4.5 0zm0 6.3a1.8 1.8 0 1 1 0-3.6 1.8 1.8 0 0 1 0 3.6z" fill="#c8c8c8"/></svg><span style="width:170px">Lorem ipsum dolor sit amet, con-sectetur adipiscing elit.</span></div>
    <div class="touch" style="top:210px"><svg width="18" height="18" viewBox="0 0 12 12"><path d="M2.4 0.5l2 2-1 1.6c.7 1.5 1.9 2.7 3.5 3.5l1.6-1 2 2-1.2 2.2C5.3 10.6 1.4 6.7.2 1.7z" fill="#c8c8c8"/></svg><span>+(1) 234 567 8900</span></div>
    <div class="touch" style="top:246px"><svg width="18" height="14" viewBox="0 0 13 10"><rect width="13" height="10" rx="1" fill="#c8c8c8"/><path d="M0.5 1l6 4.5 6-4.5" stroke="#fff" fill="none"/></svg><span>info@example.com</span></div>

    <div class="rule"></div>
    <p class="copy">Copyrights 2020 BRISTLEWOOD PETS • All Rights Reserved.</p>
  </footer>

</div>
</body>
</html>
```